Stationery - business cards, headers/footers, powerpoint templates
2 sets of business cards. One for 'Owen Tasker' and one for 'Lars Pemberton'. No job titles needed
Stationery - business cards, headers/footers, powerpoint templates - Consulting
Creative Brief
Simple
1. Lars Pemberton 2. Owen Tasker
Grand Cayman Cayman Islands
Lars@coverloom.ky
coverloom.ky
2 sets of business cards required - one for Lars Pemberton and one for Owen TAsker. Note that our email addresses are Lars@coverloom.ky and Owen@coverloom.ky
Modern/clean logo

```html
<!DOCTYPE html>
<html lang="en">
<head>
<meta charset="UTF-8">
<title>Coverloom Business Cards</title>
<link href="https://fonts.googleapis.com/css2?family=Montserrat:wght@700&family=Open+Sans:wght@400;600&display=swap" rel="stylesheet">
<style>
  :root {
    --stage: #2b2b2d;
    --card-dark: #0b0b0c;
    --card-light: #ffffff;
    --ink-light: #ffffff;
    --ink-dark: #2a2a2a;
    --ink-muted: #5f5f63;
    --accent: #f05bb7;
  }
  * { margin: 0; padding: 0; box-sizing: border-box; }
  html, body {
    width: 1200px;
    height: 768px;
    overflow: hidden;
    background: var(--stage);
  }
  .canvas {
    width: 1200px;
    height: 768px;
    display: flex;
    align-items: center;
    justify-content: center;
    gap: 60px;
  }
  .card {
    position: relative;
    width: 500px;
    height: 286px;
    border-radius: 4px;
    box-shadow: 0 10px 30px rgba(0,0,0,0.35);
  }
  .card--front {
    background: var(--card-dark);
    display: flex;
    align-items: center;
    justify-content: center;
  }
  .card--back {
    background: var(--card-light);
  }
  .brand-name {
    font-family: "Montserrat", sans-serif;
    font-weight: 700;
    letter-spacing: -0.5px;
    line-height: 1;
  }
  .card--front .brand-name {
    color: var(--ink-light);
    font-size: 56px;
  }
  .card--back .brand-name {
    position: absolute;
    top: 46px;
    right: 36px;
    color: var(--ink-dark);
    font-size: 36px;
  }
  .contact {
    position: absolute;
    left: 36px;
    right: 36px;
    bottom: 50px;
    font-family: "Open Sans", sans-serif;
    color: var(--ink-muted);
    font-size: 12.5px;
    line-height: 1.6;
    white-space: nowrap;
  }
  .contact__name {
    font-weight: 600;
    color: var(--accent);
    font-size: 19px;
    line-height: 1.3;
    margin-bottom: 6px;
  }
</style>
</head>
<body>
  <main class="canvas">
    <section class="card card--front">
      <div class="brand-name">coverloom</div>
    </section>
    <section class="card card--back">
      <div class="brand-name">coverloom</div>
      <div class="contact">
        <div class="contact__name">Lars Pemberton</div>
        <div class="contact__address">Harbour Point, Seven Mile Bay</div>
        <div class="contact__lines">C. +1(555) 214-0386 &nbsp;E. Lars@coverloom.ky &nbsp;www.coverloom.ky</div>
      </div>
    </section>
  </main>
</body>
</html>
```